Financial Advisor needs a NEW business card design

We need a new card design as our current design has no white space and clients tend to want to write on the card. I am attaching our current logos and current card design. I have also played with some designs I liked online but don't have the knowledge (or software) to complete the designs in a format that is appropriate for production. I've attached those designs that I liked too. With two office locations and a disclaimer there is a lot of info but we want it to look tidy. We like the deep, rich blue colors and want it to look clean, strong, and modern yet classic.
Business
Included in the attached files

```html
<!DOCTYPE html>
<html lang="en">
<head>
<meta charset="utf-8">
<title>Halvern Financial Advisory – Business Card</title>
<link href="https://fonts.googleapis.com/css2?family=Cinzel:wght@500;600&family=Open+Sans:wght@400;600&display=swap" rel="stylesheet">
<style>
  :root {
    --navy: #0b2a48;
    --navy-deep: #082239;
    --paper: #f4f4f2;
    --white: #ffffff;
    --backdrop: #d9d9d7;
    --muted-white: #dfe6ee;
  }
  * { margin: 0; padding: 0; box-sizing: border-box; }
  html, body { width: 1200px; height: 1029px; overflow: hidden; }
  body {
    background: var(--backdrop);
    position: relative;
    font-family: "Open Sans", Arial, sans-serif;
  }
  .card {
    position: absolute;
    left: 220px;
    width: 760px;
    height: 434px;
    border-radius: 4px;
    box-shadow: 0 6px 18px rgba(0,0,0,0.18);
  }
  .card--back { top: 60px; background: var(--navy-deep); color: var(--white); }
  .card--front { top: 535px; background: var(--paper); color: var(--navy); }

  .brand-name {
    font-family: "Cinzel", "Times New Roman", serif;
    font-weight: 600;
    text-transform: uppercase;
    line-height: 1.15;
    letter-spacing: 1px;
  }
  .card--back .brand-name {
    position: absolute;
    top: 120px; left: 0; right: 0;
    text-align: center;
    font-size: 38px;
    color: var(--white);
  }
  .disclaimer {
    position: absolute;
    top: 268px; left: 100px; right: 100px;
    text-align: center;
    font-size: 11.5px;
    letter-spacing: 2px;
    line-height: 1.6;
    text-transform: uppercase;
    color: var(--muted-white);
  }

  .card--front .brand-name {
    position: absolute;
    top: 56px; left: 60px;
    font-size: 36px;
    color: var(--navy);
  }
  .person {
    position: absolute;
    top: 200px; left: 440px;
    font-family: "Cinzel", "Times New Roman", serif;
    color: var(--navy);
  }
  .person__name { font-size: 22px; font-weight: 600; letter-spacing: 3px; }
  .person__role { font-size: 14px; font-weight: 500; letter-spacing: 4px; margin-top: 2px; }

  .contact {
    position: absolute;
    font-size: 13px;
    line-height: 1.45;
    color: var(--navy);
  }
  .contact--left { top: 258px; left: 60px; }
  .contact--right { top: 318px; left: 440px; }
  .contact__row { display: flex; align-items: flex-start; gap: 12px; margin-bottom: 10px; }
  .contact__icon { width: 14px; height: 14px; margin-top: 2px; flex: none; fill: var(--navy); }
</style>
</head>
<body>

<section class="card card--back">
  <div class="brand-name">Halvern<br>Financial Advisory</div>
  <p class="disclaimer">Investment advisor services offered through Northgate Private Capital, LLC, an SEC registered investment advisor</p>
</section>

<section class="card card--front">
  <div class="brand-name">Halvern<br>Financial Advisory</div>

  <div class="person">
    <div class="person__name">MARCUS DELANEY</div>
    <div class="person__role">FINANCIAL ADVISOR</div>
  </div>

  <div class="contact contact--left">
    <div class="contact__row">
      <svg class="contact__icon" viewBox="0 0 24 24" aria-hidden="true"><path d="M6.6 10.8a15.1 15.1 0 0 0 6.6 6.6l2.2-2.2a1 1 0 0 1 1-.25 11.4 11.4 0 0 0 3.6.57 1 1 0 0 1 1 1V20a1 1 0 0 1-1 1A17 17 0 0 1 3 4a1 1 0 0 1 1-1h3.5a1 1 0 0 1 1 1c0 1.25.2 2.45.57 3.57a1 1 0 0 1-.25 1z"/></svg>
      <div>555-210-4480 riverton<br>555-388-1926 lakemont</div>
    </div>
    <div class="contact__row">
      <svg class="contact__icon" viewBox="0 0 24 24" aria-hidden="true"><path d="M12 2a7 7 0 0 0-7 7c0 5.2 7 13 7 13s7-7.8 7-13a7 7 0 0 0-7-7zm0 9.5A2.5 2.5 0 1 1 12 6.5a2.5 2.5 0 0 1 0 5z"/></svg>
      <div>2840 Harbor Lane, Suite 410<br>Riverton, Texas 75001</div>
    </div>
  </div>

  <div class="contact contact--right">
    <div class="contact__row">
      <svg class="contact__icon" viewBox="0 0 24 24" aria-hidden="true"><circle cx="12" cy="12" r="10"/></svg>
      <div>marcus@halvernfinancial.com<br>WWW.HALVERNFINANCIAL.COM</div>
    </div>
    <div class="contact__row">
      <svg class="contact__icon" viewBox="0 0 24 24" aria-hidden="true"><path d="M12 2a7 7 0 0 0-7 7c0 5.2 7 13 7 13s7-7.8 7-13a7 7 0 0 0-7-7zm0 9.5A2.5 2.5 0 1 1 12 6.5a2.5 2.5 0 0 1 0 5z"/></svg>
      <div>77 Cedar Park Blvd. Suite 630<br>Lakemont, Texas 75090</div>
    </div>
  </div>
</section>

</body>
</html>
```